Food Platform with Economic-Social Cause, needs folder design, corporate and stationery

Technology company linked to food with strong social commitment, needs to dazzle customers and shareholders, with elegant, minimalist and distinguished design of folder, corporate card and other stationery. The Company proposes networking by creating a community committed to the economic and social aspects. The humanization of the economy. We attach a model of another company card and logo to use in proposals.
UNFORTUNATELY WE CANNOT FIND A DESIGN THAT DOES NOT REPRESENT WHAT WE ARE LOOKING FOR
Target Market(s)
Companies, entrepreneurs, food producers and the general public
Industry/Entity Type
Food companies, Foundations fight against hunger, Citizenship.
Colors
Designer to choose colors to be used in the design.
Requirements
Must have
- elegance, minimalism, graphic communication of networking for a humanized economy. phrase "activating consciousness" "united for a cause"
Nice to have
- human network graph. Chain of favors. Preferred shades: white, gold or champagne and combination.human network graph. Chain of favors. Preferred shades: white, gold or champagne and combination.
Should not have
- dark communication

```html
<!DOCTYPE html>
<html lang="en">
<head>
<meta charset="UTF-8">
<title>Food Logistics Triple Impact Technology – Folder Cover</title>
<link href="https://fonts.googleapis.com/css2?family=Montserrat:wght@300;400;600;800&display=swap" rel="stylesheet">
<style>
  :root {
    --cover-taupe: #6e6260;
    --cover-taupe-deep: #5f5452;
    --panel-white: #f4f3f1;
    --network-light: #e9e7e4;
    --network-mid: #d3cfcb;
    --text-white: #ffffff;
    --text-soft: #e4dedb;
    --rule: rgba(255,255,255,0.45);
  }
  * { margin: 0; padding: 0; box-sizing: border-box; }
  html, body { width: 831px; height: 1200px; overflow: hidden; background: #ffffff; }
  .folder-cover {
    position: relative;
    width: 831px; height: 1200px;
    background: linear-gradient(160deg, var(--cover-taupe) 0%, var(--cover-taupe-deep) 100%);
    font-family: "Montserrat", sans-serif;
    color: var(--text-white);
    overflow: hidden;
  }
  .cover-shapes { position: absolute; inset: 0; }
  .cover-title {
    position: absolute; left: 70px; top: 720px;
    line-height: 1.08;
  }
  .cover-title .title-strong {
    display: block; font-weight: 800; font-size: 46px; letter-spacing: 0.5px;
  }
  .cover-title .title-light {
    display: block; font-weight: 300; font-size: 46px; letter-spacing: 2px; margin-top: 2px;
  }
  .cover-lede {
    position: absolute; left: 70px; top: 900px; width: 360px;
    font-size: 14px; line-height: 1.5; color: var(--text-soft); font-weight: 400;
  }
  .cover-contact {
    position: absolute; left: 70px; right: 70px; bottom: 70px;
    display: flex; align-items: flex-start; gap: 28px;
    font-size: 13px; color: var(--text-soft);
  }
  .contact-phone { padding-right: 28px; border-right: 1px solid var(--rule); line-height: 1.6; }
  .contact-label { display: block; font-weight: 600; color: var(--text-white); }
  .contact-web { line-height: 1.6; }
  .contact-note { display: block; margin-top: 4px; font-size: 11px; max-width: 300px; line-height: 1.45; }
</style>
</head>
<body>
  <main class="folder-cover">
    <svg class="cover-shapes" width="831" height="1200" viewBox="0 0 831 1200" aria-hidden="false">
      <defs>
        <linearGradient id="networkTone" x1="0" y1="0" x2="1" y2="1">
          <stop offset="0" stop-color="var(--network-light)"/>
          <stop offset="1" stop-color="var(--network-mid)"/>
        </linearGradient>
      </defs>
      <polygon class="white-panel" points="0,0 831,0 831,340 560,650 0,590" fill="var(--panel-white)"/>
      <polygon class="network-image" role="img"
        aria-label="Photo of many small people standing on a white floor, joined by thin lines into a network graph"
        points="40,40 791,40 791,330 556,600 40,548" fill="url(#networkTone)"/>
    </svg>

    <h1 class="cover-title">
      <span class="title-strong">FOOD LOGISTICS</span>
      <span class="title-strong">TRIPLE IMPACT</span>
      <span class="title-light">TECHNOLOGY</span>
    </h1>

    <p class="cover-lede">Activating consciousness, united for a cause across every link of the food chain.</p>

    <footer class="cover-contact">
      <div class="contact-phone">
        <span class="contact-label">Contact Us</span>
        01-800-517-264
      </div>
      <div class="contact-web">
        hello@trimpactfood.org<br>
        www.trimpactfood.org
        <span class="contact-note">Connecting producers, companies and people in one humanized network.</span>
      </div>
    </footer>
  </main>
</body>
</html>
```